The Willowbank Clinic :

At The Willowbank Clinic our goal is to provide the most skilled and advanced examination and treatment of the upper neck for superior long-term outcomes for those experiencing headache or migraine.

If a spinal disorder is responsible for the headache and migraine condition the disorder will involve one or more of the top three spinal segments. The fundamental and most powerful feature of The Willowbank Clinic is our method of examining the movements of the top three spinal segments.

We would like the design should communicate professionalism and specialisation.
Updates

Don't necessarily have to have the photos provided.Photo was used for promotional material. I dont have a logo as yet what I  would also like designed.

Project Deadline Extended
Reason: Opening has been delayed due to construction issues of building.

Industry/Entity Type

Clinic

Contact Information for Business Card

The Willowbank Clinic
Suite 4, Larchford Heath Centre
87 Tollbury Drive, Kelsford Bay NSW 2519
Tel : 63 27 1846 www.thewillowbankclinic.com.au

Requirements
Must have
• Mr Colin Hartwell
Senior Physiotherapist / Senior Accredited Exercise Physiologist
Ba. App. Sc. (Physiotherapy), Ba Sp. Sc. (Exercise Science), Dip. R.M, MRTA, MUPGA, MVTB, MBRLK.

Appointment area on back of card

```html
<!DOCTYPE html>
<html lang="en">
<head>
<meta charset="utf-8">
<title>The Willowbank Clinic – Business Card</title>
<link rel="stylesheet" href="https://fonts.googleapis.com/css2?family=Source+Sans+3:wght@400;600&display=swap">
<style>
  :root {
    --backdrop: #2c2c2c;
    --clinic-green: #abc92a;
    --paper: #ffffff;
    --ink: #1e1e1e;
    --photo-light: #f3ece6;
    --photo-mid: #e6cdb8;
    --photo-warm: #d9b98f;
  }
  * { box-sizing: border-box; margin: 0; padding: 0; }
  html, body {
    width: 1200px; height: 900px; overflow: hidden;
    background: var(--backdrop);
    font-family: "Source Sans 3", "Myriad Pro", Arial, sans-serif;
  }
  .card {
    position: absolute; top: 292px;
    width: 513px; height: 314px;
    overflow: hidden;
  }
  .card-front { left: 73px; background: var(--clinic-green); }
  .card-back { left: 615px; background: var(--paper); }

  .wordmark {
    display: flex; align-items: center; gap: 12px;
    font-weight: 600; letter-spacing: 0.5px; white-space: nowrap;
  }
  .wordmark-dot { border-radius: 50%; flex: none; }
  .card-front .wordmark {
    position: absolute; left: 96px; top: 134px;
    color: var(--paper); font-size: 28px;
  }
  .card-front .wordmark-dot {
    width: 44px; height: 44px; border: 4px solid var(--paper);
  }
  .card-back .wordmark {
    position: absolute; left: 29px; top: 34px;
    color: var(--ink); font-size: 21px;
  }
  .card-back .wordmark-dot {
    width: 38px; height: 38px; border: 4px solid var(--clinic-green);
  }

  .portrait {
    position: absolute; right: 0; top: 0;
    width: 166px; height: 194px;
    background: linear-gradient(90deg, var(--paper) 0%, var(--photo-light) 25%, var(--photo-mid) 60%, var(--photo-warm) 100%);
  }

  .contact {
    position: absolute; left: 52px; top: 103px;
    color: var(--ink); font-size: 11px; line-height: 15px;
  }
  .contact-name { font-size: 14px; margin-bottom: 3px; }
  .contact-line { display: flex; align-items: flex-start; gap: 6px; }
  .contact-line svg { width: 9px; height: 9px; margin-top: 3px; flex: none; }
  .contact-line .indent { padding-left: 15px; }

  .staff-band {
    position: absolute; left: 0; bottom: 0;
    width: 100%; height: 120px;
    background: var(--clinic-green);
    color: var(--paper);
    padding: 22px 0 0 52px;
  }
  .staff-name { font-size: 25px; line-height: 28px; font-weight: 400; margin-bottom: 4px; }
  .staff-credentials { font-size: 9.5px; line-height: 13px; font-weight: 600; }
</style>
</head>
<body>
  <section class="card card-front" aria-label="Card front">
    <div class="wordmark"><span class="wordmark-dot"></span>The Willowbank Clinic</div>
  </section>

  <section class="card card-back" aria-label="Card back">
    <div class="wordmark"><span class="wordmark-dot"></span>The Willowbank Clinic</div>

    <div class="portrait" role="img" aria-label="Portrait photo of a smiling woman"></div>

    <div class="contact">
      <p class="contact-name">The Willowbank Clinic</p>
      <p class="contact-line">
        <svg viewBox="0 0 10 10" aria-hidden="true"><path d="M5 0.5 L10 5 H8.5 V9.5 H6 V6.5 H4 V9.5 H1.5 V5 H0 Z" fill="currentColor"/></svg>
        <span>Suite 4, Larchford Heath Centre</span>
      </p>
      <p class="contact-line"><span class="indent">87 Tollbury Drive, Kelsford Bay NSW 2519</span></p>
      <p class="contact-line">
        <svg viewBox="0 0 10 10" aria-hidden="true"><path d="M1 3 Q5 0 9 3 L8 4.5 L6.5 4 V3.3 Q5 3 3.5 3.3 V4 L2 4.5 Z M2 5.5 H8 L9 9.5 H1 Z" fill="currentColor"/></svg>
        <span>63 27 1846</span>
      </p>
      <p class="contact-line">
        <svg viewBox="0 0 10 10" aria-hidden="true" fill="none" stroke="currentColor" stroke-width="1"><circle cx="5" cy="5" r="4.3"/><ellipse cx="5" cy="5" rx="1.8" ry="4.3"/><path d="M0.7 5 H9.3 M1.5 2.8 H8.5 M1.5 7.2 H8.5"/></svg>
        <span>www.thewillowbankclinic.com.au</span>
      </p>
    </div>

    <div class="staff-band">
      <h1 class="staff-name">Mr Colin Hartwell</h1>
      <p class="staff-credentials">Senior Physiotherapist / Senior Accredited Exercise Physiologist<br>
      Ba. App. Sc. (Physiotherapy), Ba Sp. Sc. (Exercise Science),<br>
      Dip. R.M, MRTA, MUPGA, MVTB, MBRLK.</p>
    </div>
  </section>
</body>
</html>
```